Business and Success Coaching Business Card

Need a business card for my coaching business. I coach small businesses, career professionals and, individuals wanting to unlock their human potential and achieve excellence. At the heart of our methodology is the Shaping Purposeful Action Routines Knowingly (SPARK) approach to formulate empowerment, create principles for success and setting achievable outcomes. I would like something that incorporates our new logo, something clean and sharp with a solid darker, but complementary background, color on the card front. The back should be white where there will be room for three questions

Target Market(s)

People looking to advance and improve themselves through a success coach

Industry/Entity Type

Life Coaching

Contact Information for Business Card

Contact information on card.
Business name on front of card
Questions on back

Font styles to use
Other font styles liked:
• Century Gothic or other Serif style fonts that look similar to Century Gothic

Colors

Designer to choose colors to be used in the design.

Requirements
Must have
• Logo on front of card
• Business name - The Steady Forge
• Contact name - Ted Harlow
• Address - Box 4619, Littleton, CO 80127-4619
• Phone number - 303-555-0147
• Email address - harlow.ted@thesteadyforge.example
• Certifications - CSC, CCHt, PTT, PNLP
• Back of card
• Three questions on the back of the card:
• If you were at your best, what would you do right now?
• What is the decision you have been avoiding?
• What's one action you could take in the next 10 minutes?
Nice to have
• I would like to see a solid color on the front of the card that compliments the logo.
• Back should be white, or could be contrasting, but need to have the three questions.

```html
<!DOCTYPE html>
<html lang="en">
<head>
<meta charset="utf-8">
<title>The Steady Forge – Business Card</title>
<link rel="stylesheet" href="https://fonts.googleapis.com/css2?family=Montserrat:wght@600;700&family=Questrial&display=swap">
<style>
  :root {
    --navy: #1f3a7f;
    --navy-deep: #1b3372;
    --navy-soft: #27468e;
    --sky: #4a86c8;
    --sky-pale: #a9c3e2;
    --mist: #c5d4e6;
    --paper: #ffffff;
    --backdrop: #2a2a2e;
  }
  * { box-sizing: border-box; margin: 0; padding: 0; }
  html, body { width: 1200px; height: 800px; overflow: hidden; }
  body {
    background: var(--backdrop);
    position: relative;
    font-family: "Questrial", "Century Gothic", sans-serif;
  }
  .card {
    position: absolute;
    width: 520px;
    height: 297px;
    border-radius: 4px;
    overflow: hidden;
    box-shadow: 0 14px 30px rgba(0,0,0,.45);
  }
  .brand-name {
    font-family: "Montserrat", "Century Gothic", sans-serif;
    font-weight: 700;
    letter-spacing: -0.5px;
    line-height: 1;
    white-space: nowrap;
  }
  .tagline { white-space: nowrap; }

  /* Front: solid navy */
  .card--front {
    left: 60px; top: 170px;
    background: var(--navy);
    color: var(--paper);
  }
  .front-mark {
    position: absolute;
    right: 70px; top: 20px;
    width: 170px; height: 150px;
  }
  .front-content {
    position: relative;
    padding: 64px 40px 0 44px;
  }
  .card--front .brand-name { font-size: 38px; }
  .card--front .tagline {
    font-size: 21px;
    margin-top: 4px;
    margin-left: 44px;
    color: var(--mist);
  }
  .questions {
    list-style: none;
    margin-top: 34px;
    font-size: 15px;
    line-height: 1.55;
    color: var(--mist);
  }
  .questions li:nth-child(2) { padding-left: 30px; }

  /* Back: white with contact details */
  .card--back {
    left: 620px; top: 330px;
    background: var(--paper);
    color: var(--navy-deep);
  }
  .back-art {
    position: absolute;
    inset: 0;
    width: 520px; height: 297px;
  }
  .back-brand {
    position: absolute;
    left: 28px; top: 62px;
  }
  .card--back .brand-name { font-size: 30px; color: var(--navy-deep); }
  .card--back .tagline {
    font-size: 16px;
    color: var(--mist);
    margin-left: 36px;
    margin-top: 2px;
  }
  .contact {
    position: absolute;
    left: 60px; top: 136px;
    font-size: 12.5px;
    line-height: 1.4;
  }
  .contact-name {
    font-family: "Montserrat", "Century Gothic", sans-serif;
    font-weight: 700;
    font-size: 17px;
    margin-bottom: 6px;
  }
  .contact-address { margin-bottom: 4px; }
  .contact-line { display: flex; align-items: center; gap: 6px; white-space: nowrap; }
  .contact-line svg { width: 12px; height: 12px; flex: none; }
  .certs { margin-top: 6px; }
  .certs-label {
    font-family: "Montserrat", "Century Gothic", sans-serif;
    font-weight: 700;
  }
</style>
</head>
<body>

<section class="card card--front">
  <svg class="front-mark" viewBox="0 0 170 150" role="img" aria-label="Faint background area for the leaping figure emblem">
    <rect x="0" y="0" width="170" height="150" rx="10" fill="var(--navy-soft)" opacity="0.55"/>
  </svg>
  <div class="front-content">
    <h1 class="brand-name">The Steady Forge</h1>
    <p class="tagline">Jump-start your next phase</p>
    <ul class="questions">
      <li>If you were at your best, what would you do right now?</li>
      <li>What is the decision you have been avoiding?</li>
      <li>What's one action you could take in the next 10 minutes?</li>
    </ul>
  </div>
</section>

<section class="card card--back">
  <svg class="back-art" viewBox="0 0 520 297" aria-hidden="false">
    <path class="hill" d="M318,297 C338,250 348,205 378,175 C404,150 402,128 432,117 C462,106 492,100 520,92 L520,297 Z" fill="var(--navy-deep)"/>
    <rect class="figure-area" x="352" y="16" width="150" height="94" rx="8" fill="var(--sky-pale)" role="img" aria-label="Illustration area: leaping figure with light rays above the hill"/>
  </svg>

  <div class="back-brand">
    <h2 class="brand-name">The Steady Forge</h2>
    <p class="tagline">Jump-start your next phase</p>
  </div>

  <div class="contact">
    <p class="contact-name">Ted Harlow</p>
    <p class="contact-address">Box 4619, Littleton<br>CO 80127-4619</p>
    <p class="contact-line">
      <svg viewBox="0 0 12 12" aria-hidden="true"><circle cx="6" cy="6" r="6" fill="#4a86c8"/><path d="M4 3.2l1 1.4-.6.7c.4.8 1 1.4 1.8 1.8l.7-.6 1.4 1-.5 1c-2.4-.2-4.4-2.2-4.6-4.6z" fill="#fff"/></svg>
      303-555-0147
    </p>
    <p class="contact-line">
      <svg viewBox="0 0 12 12" aria-hidden="true"><circle cx="6" cy="6" r="6" fill="#4a86c8"/><rect x="3" y="4" width="6" height="4.2" fill="#fff"/><path d="M3 4l3 2.3L9 4" stroke="#4a86c8" stroke-width=".7" fill="none"/></svg>
      harlow.ted@thesteadyforge.example
    </p>
    <p class="certs"><span class="certs-label">Certifications:</span><br>CSC, CCHt, PTT, PNLP</p>
  </div>
</section>

</body>
</html>
```